Tap Nest Flow is an under sink water filtration product for the domestic market which will replace the need to purchase bottled water in the home.

The water filter provides safe delicious drinking water at the kitchen sink.

Priced at €2.99 per week

I am looking for a series of five flyers.

Re-develope the attached one and we will get you to develop a series of five more.
Updates

To Designers

This is my first time using this service and therefore is a test with a small investment. None of the designs posted so far are up to the standard required. I do like the parachute idea but would need to be more finished. The original flyer provided with the original brief is without doubt the best by far. 
I am not sure what the next step is however I cannot use anything produced so far.

Target Market(s)

Domestic home owner.

Requirements
Must have
• See attached example
Nice to have
• See attached

```html
<!DOCTYPE html>
<html lang="en">
<head>
<meta charset="utf-8">
<title>Tap Nest Flow – Flyer</title>
<link rel="stylesheet" href="https://fonts.googleapis.com/css2?family=Anton&family=Oswald:wght@500;700&family=Roboto+Condensed:wght@700&display=swap">
<style>
  :root {
    --navy: #1b2a6b;
    --frame: #17245e;
    --sky: #2f86d6;
    --mint: #c9ecd3;
    --yellow: #ffe21a;
    --orange: #f07a12;
    --white: #ffffff;
    --list-bg: #bcd8f1;
    --red: #d4142a;
    --strip: #eef2f7;
    --rose: #c2186b;
    --rose-light: #e88db4;
    --skin: #e8b99a;
    --hand: #e9b84a;
  }
  * { box-sizing: border-box; margin: 0; padding: 0; }
  html, body { width: 995px; height: 1200px; overflow: hidden; background: var(--white); }
  .flyer {
    position: relative;
    width: 995px;
    height: 1200px;
    background: var(--sky);
    border: 12px solid var(--frame);
    overflow: hidden;
    font-family: "Roboto Condensed", Arial, sans-serif;
  }
  .header-panel {
    position: absolute;
    left: 0; top: 0;
    width: 971px; height: 418px;
    background: var(--mint);
    border-bottom: 6px solid var(--frame);
    overflow: hidden;
  }
  .mascot-art {
    position: absolute;
    left: 30px; top: 165px;
    width: 140px; height: 230px;
    border-radius: 40px;
    background: linear-gradient(160deg, #ffffff, #cfd8e3);
  }
  .hand-art {
    position: absolute;
    left: 430px; top: 0;
    width: 220px; height: 250px;
    border-radius: 0 0 100px 100px;
    background: linear-gradient(180deg, var(--hand), #c98f2a);
  }
  .brand-name {
    position: absolute;
    font-family: "Anton", "Arial Black", sans-serif;
    font-size: 96px;
    line-height: 1.1;
    color: var(--navy);
    letter-spacing: 3px;
  }
  .brand-name--top { left: 140px; top: 30px; }
  .brand-name--mid { left: 220px; top: 150px; }
  .brand-name--low { left: 190px; top: 275px; }
  .tagline {
    position: absolute;
    left: 520px; top: 180px;
    width: 440px;
    transform: rotate(14deg);
    transform-origin: left top;
    font-family: "Oswald", Arial, sans-serif;
    font-weight: 700;
    font-size: 33px;
    line-height: 1.1;
    color: var(--navy);
    text-align: center;
    text-transform: uppercase;
    font-style: italic;
    white-space: nowrap;
  }
  .headline {
    position: absolute;
    left: 28px; top: 438px;
    width: 920px;
    font-family: "Oswald", Arial, sans-serif;
    font-weight: 700;
    font-size: 27px;
    color: var(--yellow);
    text-transform: uppercase;
  }
  .intro {
    position: absolute;
    left: 50px; top: 480px;
    width: 860px;
    font-size: 27px;
    line-height: 1.3;
    color: var(--white);
  }
  .woman-art {
    position: absolute;
    left: 600px; top: 600px;
    width: 371px; height: 580px;
    border-radius: 180px 180px 0 0;
    background: linear-gradient(180deg, var(--rose) 0%, var(--rose-light) 45%, var(--skin) 65%, var(--rose) 100%);
  }
  .slogan {
    position: absolute;
    left: 50px; top: 630px;
    font-family: "Anton", "Arial Black", sans-serif;
    font-size: 78px;
    line-height: 1.1;
    color: var(--yellow);
    letter-spacing: 5px;
    transform: rotate(3deg);
    -webkit-text-stroke: 2px var(--orange);
  }
  .contaminant-list {
    position: absolute;
    left: 40px; top: 755px;
    width: 650px; height: 170px;
    background: var(--list-bg);
    border: 4px solid var(--red);
    border-radius: 18px;
    padding: 10px 20px;
    display: flex;
    flex-wrap: wrap;
    justify-content: center;
    align-content: center;
    gap: 2px 34px;
    list-style: none;
  }
  .contaminant-list li {
    font-family: "Oswald", Arial, sans-serif;
    font-weight: 700;
    font-size: 26px;
    line-height: 1.3;
    color: var(--navy);
    text-decoration: line-through;
    text-decoration-color: var(--red);
    text-decoration-thickness: 3px;
  }
  .benefits {
    position: absolute;
    left: 50px; top: 980px;
    font-size: 30px;
    line-height: 1.25;
    color: var(--white);
  }
  .contact-strip {
    position: absolute;
    left: 0; top: 1080px;
    width: 690px; height: 96px;
    background: var(--strip);
    padding: 8px 0 0 48px;
    color: var(--red);
  }
  .contact-strip .lead { font-size: 32px; line-height: 1.1; }
  .contact-strip .phone { font-size: 36px; letter-spacing: 2px; padding-left: 150px; }
  .price-badge {
    position: absolute;
    left: 580px; top: 860px;
    width: 220px; height: 220px;
  }
</style>
</head>
<body>
<main class="flyer">
  <header class="header-panel">
    <div class="mascot-art" role="img" aria-label="Cartoon water bottle character running away"></div>
    <div class="hand-art" role="img" aria-label="Illustrated hand reaching down"></div>
    <span class="brand-name brand-name--top">TAP</span>
    <span class="brand-name brand-name--mid">NEST</span>
    <span class="brand-name brand-name--low">FLOW</span>
    <p class="tagline">Making your tap water<br>safe &amp; delicious<br>to drink</p>
  </header>

  <h1 class="headline">Sick and tired of having to buy expensive plastic bottled water?</h1>
  <p class="intro">Then, save on your weekly shopping with the new affordable TAP NEST FLOW. All the delicious clean and healthy water you can drink from your tap for only €2.99 a week, Including a FREE annual filter change.</p>

  <div class="woman-art" role="img" aria-label="Illustrated woman in a pink hat and gloves"></div>

  <p class="slogan">SAY BYE! BYE!</p>

  <ul class="contaminant-list">
    <li>FOUL ODOURS</li>
    <li>SEDIMENT</li>
    <li>INSECTICIDES</li>
    <li>PESTICIDES</li>
    <li>NASTY TASTES</li>
    <li>CHLORINE</li>
    <li>ARSENIC</li>
    <li>CRYPTOSPORIDIUM</li>
    <li>LEAD</li>
    <li>TRIHALOMETHANES</li>
  </ul>

  <p class="benefits">Clean | Healthy | Affordable | Safe<br>Drinking Water without the Bottle</p>

  <footer class="contact-strip">
    <p class="lead">To find out more LoCall</p>
    <p class="phone">1890 555 014</p>
  </footer>

  <svg class="price-badge" viewBox="0 0 220 220" aria-label="Only €2.99 a week">
    <circle cx="110" cy="110" r="106" fill="var(--yellow)" stroke="var(--navy)" stroke-width="2"/>
    <g transform="rotate(-24 110 110)" fill="var(--navy)" font-family="Oswald, Arial, sans-serif" font-weight="700" text-anchor="middle">
      <text x="110" y="72" font-size="40">Only</text>
      <text x="110" y="136" font-size="62">€2.99</text>
      <text x="110" y="180" font-size="36">week</text>
    </g>
  </svg>
</main>
</body>
</html>
```